Kick Ass, Edgy, Fun, E commerce Embroidery Company Business Card

Sleek and edgy business card layout. main logo on front with business description (Custom Embroidery, the file is submitted is supposed to look like stitching)
Name, address, phone numbers, social icons (Facebook and Instagram) on back. The card will be black plastic and the front main logo will be printed Spot UV.

Target Market(s)

Small Business Owners

Contact Information for Business Card

Focused, not cluttered and sleek. Modern looking.

Font styles to use
Other font styles liked:
• Very clean and elegant

Colors
acd136

Requirements
Must have
• Custom Embroidery

our Tagline: Every Logo Has A Story - Thread Yours
Nice to have
• Social Icons for Facebook and Instagram
Should not have
• Too much visual noise

```html
<!DOCTYPE html>
<html lang="en">
<head>
<meta charset="utf-8">
<title>Stitchforge Business Card</title>
<link rel="stylesheet" href="https://fonts.googleapis.com/css2?family=Russo+One&family=Ubuntu:wght@400;700&display=swap">
<style>
  :root {
    --stage: #d6d6d6;
    --card: #161616;
    --card-edge: #1e1e1e;
    --green: #acd136;
    --green-deep: #4aa83a;
    --white: #f2f2f2;
    --grey: #6d6d6d;
  }
  * { box-sizing: border-box; margin: 0; padding: 0; }
  html, body { width: 1200px; height: 900px; overflow: hidden; }
  body {
    background: var(--stage);
    display: flex;
    align-items: center;
    justify-content: center;
    gap: 48px;
    font-family: "Ubuntu", sans-serif;
  }
  .card {
    position: relative;
    width: 540px;
    height: 309px;
    border-radius: 22px;
    background: linear-gradient(135deg, var(--card-edge), var(--card));
    box-shadow: 0 12px 28px rgba(0,0,0,.35);
    overflow: hidden;
  }

  /* Front */
  .front-name {
    position: absolute;
    left: 60px;
    top: 70px;
    font-family: "Ubuntu", sans-serif;
    font-weight: 700;
    font-size: 48px;
    line-height: 1;
    color: var(--grey);
    text-transform: uppercase;
  }
  .front-service {
    position: absolute;
    left: 60px;
    top: 190px;
    font-family: "Russo One", sans-serif;
    font-size: 34px;
    line-height: 1.05;
    color: var(--green-deep);
    text-transform: uppercase;
  }

  /* Back */
  .back-brand {
    position: absolute;
    left: 44px;
    top: 72px;
    display: flex;
    align-items: center;
    gap: 14px;
  }
  .back-brand .dot {
    width: 26px; height: 26px; border-radius: 50%;
    background: var(--green-deep);
  }
  .back-brand .name {
    font-family: "Ubuntu", sans-serif;
    font-weight: 700;
    font-size: 30px;
    color: var(--white);
  }
  .tagline {
    position: absolute;
    left: 44px;
    bottom: 26px;
    white-space: nowrap;
    font-family: "Russo One", sans-serif;
    font-size: 20px;
    color: var(--green-deep);
  }
  .contact {
    position: absolute;
    left: 290px;
    top: 34px;
    width: 220px;
    font-size: 13px;
    color: var(--white);
    line-height: 1.35;
  }
  .contact .company {
    color: var(--green-deep);
    font-weight: 700;
    font-size: 16px;
    letter-spacing: .5px;
  }
  .contact .rule {
    height: 1px;
    background: var(--green-deep);
    margin: 9px 0;
  }
  .contact .row {
    display: flex;
    align-items: center;
    gap: 6px;
  }
  .contact .row svg { width: 14px; height: 14px; flex: none; }
  .contact .web { font-weight: 700; }
  .social { display: flex; align-items: center; gap: 4px; }
  .social .chip {
    width: 14px; height: 14px; border-radius: 50%;
    background: var(--green-deep);
  }
</style>
</head>
<body>

  <section class="card card-front">
    <div class="front-name">Stitch<br>forge</div>
    <div class="front-service">Custom<br>Embroidery</div>
  </section>

  <section class="card card-back">
    <div class="back-brand">
      <span class="dot"></span>
      <span class="name">Stitchforge</span>
    </div>

    <div class="contact">
      <div class="company">Stitchforge Inc</div>
      <div>417 Harbor Mill Rd Ste 5</div>
      <div>Fairview, CO 80412</div>
      <div class="rule"></div>
      <div class="row">
        <svg viewBox="0 0 16 16"><circle cx="8" cy="8" r="8" fill="#4aa83a"/><path d="M5 4.5l1.6-.4.9 2-1 .8a5 5 0 0 0 2.6 2.6l.8-1 2 .9-.4 1.6c-3.6.2-6.7-2.9-6.5-6.5z" fill="#161616"/></svg>
        <span>1-800-555-0187</span>
      </div>
      <div class="row">
        <svg viewBox="0 0 16 16"><circle cx="8" cy="8" r="8" fill="#4aa83a"/><rect x="4" y="5" width="8" height="6" fill="none" stroke="#161616" stroke-width="1.2"/><path d="M4 5l4 3.5L12 5" fill="none" stroke="#161616" stroke-width="1.2"/></svg>
        <span>info@stitchforge.com</span>
      </div>
      <div class="row">
        <svg viewBox="0 0 16 16"><circle cx="8" cy="8" r="8" fill="#4aa83a"/><circle cx="8" cy="8" r="4.5" fill="none" stroke="#161616" stroke-width="1.1"/><path d="M3.5 8h9M8 3.5c-2 2.5-2 6.5 0 9M8 3.5c2 2.5 2 6.5 0 9" fill="none" stroke="#161616" stroke-width="1"/></svg>
        <span class="web">Stitchforge.com</span>
      </div>
      <div class="rule"></div>
      <div class="row social">
        <span class="chip"></span><span class="chip"></span>
        <span>&nbsp;/stitchforgelogos</span>
      </div>
    </div>

    <div class="tagline">Every Stitch Tells It Loud – Wear Yours</div>
  </section>

</body>
</html>
```